Need a business card design. I am a Self Empowerment Life Coach.

A Life Coach is - a professional relationship designed to enhance an individual's ability to focus, make effective changes, develop oneself, achieve desired goals and maximize success in life. Coaching is about getting the very best out of someone and enabling them to make decisions that will improve their life. It is a unique way to help people look at where they are now and where they would like to be, and helps bridge the gap.

Bright Path Coaching is motivational, inspiring, positive, exciting and action driven. By raising awareness and encouraging others to take responsibility for their life, coaching can help people rise to their challenge and go further than you ever thought possible.

Industry/Entity Type

Business

Other font styles liked:
• Bookman Old Style

Requirements
Must have
• Marla Thorncastle, QTV-AR
• Self Empowerment Coach
• 318.557.6021
• mt@thebloomingpathcoach.example
• The attached logo
Nice to have
• I would like to see some designs portrait and some landscape

```html
<!DOCTYPE html>
<html lang="en">
<head>
<meta charset="utf-8">
<title>Bright Path Coaching – Business Card</title>
<link rel="stylesheet" href="https://fonts.googleapis.com/css2?family=Exo+2:wght@400;600;700&display=swap">
<style>
  :root {
    --navy: #1d4179;
    --brand-blue: #1a86c8;
    --white: #ffffff;
    --page: #ffffff;
    --card-edge: #c9cfd8;
  }
  * { margin: 0; padding: 0; box-sizing: border-box; }
  html, body {
    width: 1144px;
    height: 1200px;
    overflow: hidden;
    background: var(--page);
  }
  .canvas {
    position: relative;
    width: 1144px;
    height: 1200px;
  }
  .card {
    position: absolute;
    left: 230px;
    top: 32px;
    width: 685px;
    height: 1168px;
    background: var(--navy);
    border: 1px solid var(--card-edge);
    font-family: "Exo 2", sans-serif;
    color: var(--white);
  }
  .logo-panel {
    position: absolute;
    left: 93px;
    top: 0;
    width: 497px;
    height: 674px;
    background: var(--white);
    display: flex;
    flex-direction: column;
    align-items: center;
    justify-content: center;
    gap: 28px;
    padding-bottom: 40px;
  }
  .brand-mark {
    width: 64px;
    height: 64px;
    border-radius: 50%;
    background: var(--brand-blue);
  }
  .brand-name {
    font-family: "Exo 2", sans-serif;
    font-weight: 700;
    font-size: 56px;
    line-height: 1.1;
    color: var(--brand-blue);
    text-align: center;
  }
  .identity {
    position: absolute;
    right: 22px;
    top: 732px;
    text-align: right;
  }
  .person-name {
    font-size: 56px;
    font-weight: 600;
    line-height: 1.05;
  }
  .credentials,
  .role {
    padding-right: 73px;
  }
  .credentials {
    font-size: 42px;
    font-weight: 400;
    line-height: 1.05;
  }
  .role {
    margin-top: 8px;
    font-size: 33px;
    font-weight: 700;
    letter-spacing: 0.5px;
  }
  .divider {
    position: absolute;
    left: 0;
    top: 920px;
    width: 685px;
    height: 60px;
  }
  .contact {
    position: absolute;
    left: 0;
    top: 1000px;
    width: 685px;
    text-align: center;
  }
  .phone {
    font-size: 38px;
    font-weight: 600;
    letter-spacing: 1px;
  }
  .email {
    margin-top: 12px;
    font-size: 30px;
    font-weight: 400;
  }
</style>
</head>
<body>
  <div class="canvas">
    <article class="card">
      <div class="logo-panel">
        <span class="brand-mark" aria-hidden="true"></span>
        <p class="brand-name">Bright Path<br>Coaching</p>
      </div>

      <div class="identity">
        <p class="person-name">Marla Thorncastle,</p>
        <p class="credentials">QTV-AR</p>
        <p class="role">Self Empowerment Coach</p>
      </div>

      <svg class="divider" viewBox="0 0 685 60" aria-hidden="true">
        <rect x="0" y="6" width="685" height="6" fill="#ffffff"/>
        <polygon points="0,22 590,22 560,50 548,42 0,42" fill="#ffffff"/>
        <polygon points="0,27 575,27 556,43 0,37" fill="#1d4179"/>
      </svg>

      <div class="contact">
        <p class="phone">318.557.6021</p>
        <p class="email">mt@thebloomingpathcoach.example</p>
      </div>
    </article>
  </div>
</body>
</html>
```